Business Cards Design for the electrical wholesaler: clean bold dynamic :)

We need a business card design that would follow our latest brand guidelines. As an electrical wholesaler we want to bring a fresh look and feel into the industry. The design should be clean bold and dynamic. It should come alive with the renewed energy of our green colour. Our grey colour should keep things balanced and complement the notion of maturity and responsibility. We employ Lato as a corporate font however are not bound by this font and we’re open to interpretation here.

Target Market(s)

Electrical contractors

Industry/Entity Type

Business

Contact Information for Business Card

Logo
Name & Surname: Olena Dovbush
Job Title: Director of Marketing
Email: helen.dovbush@mailvane.example
Cell phone: XXX.XXX.XXXX
Address: 20917 - 87 Ave. Edmonton, AB, Canada. T6K 2R8
Business Phone: 780.555.0187
Website: www.qorvil.example

Font styles to use
Other font styles liked:
• Lato

Requirements
Must have
• Logo & website
Nice to have
• Brand elements - some of them you may find in the attached Brand Guidelines (e.g. three lines on the background signifying "W")

```html
<!DOCTYPE html>
<html lang="en">
<head>
<meta charset="utf-8">
<title>Qorvil Business Cards</title>
<link rel="stylesheet" href="https://fonts.googleapis.com/css2?family=Lato:wght@100;300;400;700&display=swap">
<style>
  :root {
    --brand-green: #8dc63f;
    --brand-grey: #545557;
    --card-dark: #535456;
    --ink: #4d4e50;
    --label-ink: #2f3030;
    --white: #ffffff;
  }
  * { margin: 0; padding: 0; box-sizing: border-box; }
  html, body { width: 1200px; height: 1200px; overflow: hidden; }
  body { font-family: "Lato", Arial, sans-serif; }

  .presentation { position: relative; width: 1200px; height: 1200px; overflow: hidden; }
  .stage-top { position: absolute; left: 0; top: 0; width: 1200px; height: 600px; background: var(--brand-green); }
  .stage-bottom { position: absolute; left: 0; top: 600px; width: 1200px; height: 600px; background: var(--brand-grey); }

  .view-label {
    position: absolute; font-weight: 100; font-size: 60px; line-height: 1;
    color: var(--label-ink); letter-spacing: -0.5px;
  }
  .view-label--back { left: 206px; top: 40px; }
  .view-label--front { left: 684px; top: 1096px; color: #2a2b2b; }

  .card { position: absolute; left: 202px; width: 795px; height: 487px; overflow: hidden; }
  .card--back { top: 113px; background: var(--card-dark); }
  .card--front { top: 600px; height: 486px; background: var(--white); }

  .wordmark { position: absolute; display: flex; align-items: center; gap: 14px; font-weight: 400; line-height: 1; }
  .wordmark__square { display: block; background: var(--brand-green); }
  .card--back .wordmark { left: 50%; top: 190px; transform: translateX(-50%); color: var(--white); font-size: 96px; gap: 20px; }
  .card--back .wordmark__square { width: 56px; height: 56px; }
  .card--front .wordmark { left: 32px; top: 26px; color: var(--ink); font-size: 64px; }
  .card--front .wordmark__square { width: 38px; height: 38px; }

  .back-website {
    position: absolute; left: 0; right: 0; top: 394px; text-align: center;
    color: var(--brand-green); font-size: 20px; letter-spacing: 2px; font-weight: 400;
  }

  .person { position: absolute; left: 84px; top: 70px; }
  .person__name { font-size: 41px; font-weight: 400; color: var(--ink); letter-spacing: 0.3px; line-height: 1; margin-top: 24px; }
  .person__title {
    display: inline-block; margin-top: 14px; width: 278px; height: 27px; border-radius: 3px;
    background: var(--ink); color: var(--white); font-weight: 700; font-size: 17px;
    letter-spacing: 1px; text-align: center; line-height: 27px;
  }
  .contact-list { list-style: none; margin-top: 10px; padding-left: 24px; }
  .contact-list li { display: flex; align-items: center; gap: 11px; color: var(--ink); line-height: 1; }
  .contact-list li + li { margin-top: 7px; }
  .contact-list svg { width: 22px; height: 20px; flex: none; }
  .contact-phone { font-size: 21px; letter-spacing: 4px; }
  .contact-email { font-size: 18px; letter-spacing: 0.3px; }

  .company-info { position: absolute; left: 30px; top: 418px; color: var(--ink); font-size: 17px; letter-spacing: 1.3px; line-height: 25px; }
  .front-website { position: absolute; right: 32px; top: 428px; color: var(--ink); font-size: 17px; letter-spacing: 1.2px; }
</style>
</head>
<body>
<main class="presentation">
  <div class="stage-top"></div>
  <div class="stage-bottom"></div>

  <p class="view-label view-label--back">Back view</p>

  <section class="card card--back" aria-label="Business card back">
    <div class="wordmark"><span class="wordmark__square"></span><span>qorvil</span></div>
    <p class="back-website">www.qorvil.example</p>
  </section>

  <section class="card card--front" aria-label="Business card front">
    <div class="wordmark"><span class="wordmark__square"></span><span>qorvil</span></div>

    <div class="person">
      <h1 class="person__name">Olena Dovbush</h1>
      <p class="person__title">Director of Marketing</p>
      <ul class="contact-list">
        <li class="contact-phone">
          <svg viewBox="0 0 22 20" aria-hidden="true">
            <rect x="1" y="0" width="20" height="20" rx="4" fill="#8dc63f"/>
            <path d="M7.2 4.5 L9 4.2 L10 7 L8.8 8.2 Q10 11 12.6 12.2 L13.8 11 L16.6 12 L16.3 13.8 Q15.8 15.5 13.8 15.3 Q6.5 14 5.6 6.6 Q5.6 4.8 7.2 4.5 Z" fill="#ffffff"/>
          </svg>
          <span>XXX.XXX.XXXX</span>
        </li>
        <li class="contact-email">
          <svg viewBox="0 0 22 20" aria-hidden="true">
            <rect x="1.5" y="3" width="19" height="14" rx="1.5" fill="none" stroke="#8dc63f" stroke-width="2.2"/>
            <path d="M2.5 4.5 L11 11.5 L19.5 4.5 M2.5 16 L8.5 10 M19.5 16 L13.5 10" fill="none" stroke="#8dc63f" stroke-width="1.8"/>
          </svg>
          <span>helen.dovbush@mailvane.example</span>
        </li>
      </ul>
    </div>

    <address class="company-info" style="font-style: normal;">
      20917 - 87 Ave. Edmonton, AB, Canada. T6K 2R8<br>
      Business Phone: 780.555.0187
    </address>
    <p class="front-website">www.qorvil.example</p>
  </section>

  <p class="view-label view-label--front">Front view</p>
</main>
</body>
</html>
```